Redesign cement bags for leading cement producer in south east asia

We are from Larkfield cement and would like to redesign our bag to relaunch the product line. Our bags are made of high quality PP woven sack. We are one of the leading cement producers and we want our bags to have a Larkfield classy look on each visible side when it is loading in a truck or stacking on a pallet.

Thank you for interesting in this project. Good luck.

Project Deadline Extended Reason: Hi all, I have received requests to extend the deadline. Some of the work requires revising and some of them are still on process. To be fair, I also raise my budget to compensate the time. Thanks all for your participation. Added Sunday, July 10, 2016

Target Market(s)

Construction

Industry/Entity Type

Cement

Requirements
Must have
• You will have to design two bags for two cement grades. 52.5 is of higher grade and 42.5 is of lower grade. Both are similar in design but a distinctive colours to differentiate the two at once. Please look at Reference picture 2 for ideas.
Nice to have
• You do not have to change the original logo but the Larkfield cement word font changes are required. There are no restrictions to colours and font but please refrain from using feminine colours. Instructions on rear side of the bags are now included in the scope. Please create new layout and design new user friendly symbols.
Should not have
• Since cement is a dusty product, you need avoid some colours like black as background. The dust need to be less obvious to attract attention. Our previous base colour are shown in below.
• We want a fresh look on our bag, please do not just copy our old design and make small changes. I have attached our competitors' design, please refrain from using their design as well.
• It is recommend to do some research on cement bag sector.

```html
<!DOCTYPE html>
<html lang="en">
<head>
<meta charset="utf-8">
<title>Larkfield Cement – 42.25 Bag Dieline</title>
<link rel="stylesheet" href="https://fonts.googleapis.com/css2?family=Archivo+Black&family=Archivo:wght@400;700;800&display=swap">
<style>
:root{
  --blue:#1a9be6;
  --blue-deep:#1583c9;
  --yellow:#fec40f;
  --cream:#f8e4ae;
  --ink:#1a8fd8;
  --white:#ffffff;
  --page:#ffffff;
}
*{box-sizing:border-box;margin:0;padding:0}
html,body{width:1200px;height:1000px;overflow:hidden;background:var(--page)}
body{position:relative;font-family:"Archivo",Arial,sans-serif}
.dieline{position:absolute;left:107px;top:100px;width:580px;height:470px;transform:scale(1.7);transform-origin:0 0}
.panel{position:absolute;overflow:hidden}

/* flaps */
.flap{background:var(--blue);color:var(--white);display:flex;align-items:center;justify-content:center;gap:18px}
.flap--top{left:62px;top:5px;width:226px;height:55px;transform:rotate(180deg)}
.flap--bottom{left:352px;top:409px;width:226px;height:56px}
.flap .tag{font-size:5px;letter-spacing:2px;font-weight:700;color:var(--cream)}
.flap .grade{text-align:center;line-height:1}
.flap .grade b{display:block;font-family:"Archivo Black",sans-serif;font-size:19px;letter-spacing:.5px}
.flap .grade span{display:block;font-size:6px;letter-spacing:3px;font-weight:800;color:var(--yellow)}

/* side gussets */
.side{width:57px;height:338px;top:67px;background:var(--blue)}
.side--left{left:0}
.side--right{left:291px}
.side .band{position:absolute;left:0;top:88px;width:57px;height:162px;background:var(--yellow);display:flex;justify-content:center;gap:4px;align-items:center}
.side .band span{font-family:"Archivo Black",sans-serif;font-size:21px;color:var(--blue);letter-spacing:2px;writing-mode:vertical-rl}
.side .band span.flip{transform:rotate(180deg)}
.side .mark{position:absolute;left:0;width:57px;height:88px;display:flex;align-items:center;justify-content:center;gap:4px}
.side .mark--top{top:0}
.side .mark--bottom{top:250px}
.side .mark i{width:16px;height:16px;border-radius:50%;background:var(--cream)}
.side .mark span{font-family:"Archivo Black",sans-serif;font-size:7px;color:var(--cream);writing-mode:vertical-rl;letter-spacing:.5px}

/* front face */
.front{left:62px;top:67px;width:226px;height:338px;background:var(--blue)}
.front svg{position:absolute;inset:0}
.front .content{position:absolute;inset:0;display:flex;flex-direction:column;align-items:center}
.front .emblem{margin-top:30px;width:86px;height:86px;border-radius:50%;background:var(--blue)}
.front .brand{margin-top:10px;font-family:"Archivo Black",sans-serif;font-size:25px;color:var(--blue);letter-spacing:.5px}
.front .product{margin-top:14px;position:relative;width:156px;height:40px;display:flex;align-items:center;justify-content:center}
.front .product svg{position:absolute;inset:0}
.front .product span{position:relative;font-family:"Archivo Black",sans-serif;font-size:21px;color:var(--cream);letter-spacing:2px}
.front .origin{margin-top:18px;display:flex;align-items:center;gap:5px;font-size:7px;font-weight:800;color:var(--blue);line-height:1}
.front .origin .diamond{width:6px;height:6px;background:var(--yellow);transform:rotate(45deg)}
.weight{text-align:center;color:var(--blue);line-height:1}
.weight b{font-family:"Archivo Black",sans-serif;font-size:12px}
.weight sup{font-size:4px;font-weight:800}
.weight span{display:block;font-size:4.5px;font-weight:700}
.front .weight{margin-top:14px}
.front .spec{position:absolute;left:0;bottom:4px;width:226px;text-align:center;color:var(--blue);line-height:1.2}
.front .spec b{display:block;font-size:7.5px;font-weight:800}
.front .spec span{display:block;font-size:3.8px;font-weight:700}

/* back face */
.back{left:352px;top:67px;width:226px;height:338px;background:var(--cream);color:var(--ink)}
.back .head{display:flex;flex-direction:column;align-items:center;margin-top:12px;line-height:1}
.back .head i{width:10px;height:10px;border-radius:50%;background:var(--blue);margin-bottom:2px}
.back .head .brand-sm{font-family:"Archivo Black",sans-serif;font-size:4px}
.back .head .grade-sm{display:flex;align-items:flex-end;gap:14px;font-size:3px;font-weight:700}
.back .head .grade-sm b{font-family:"Archivo Black",sans-serif;font-size:8px}
.back .head .sub{font-size:3.5px;letter-spacing:1.5px;font-weight:800}
.info{margin:6px auto 0;width:180px;border:1px solid var(--ink);font-size:3.6px;line-height:1.15}
.info + .info{margin-top:4px}
.info h3{text-align:center;font-size:5px;font-weight:800;border-bottom:1px solid var(--ink);padding:1.5px 0}
.info .row{display:flex;align-items:center;border-top:.6px solid var(--ink);min-height:10px}
.info h3 + .row{border-top:0}
.info .row .ico{width:10px;align-self:stretch;border-right:.6px solid var(--ink);display:flex;align-items:center;justify-content:center}
.info .row .ico i{width:3px;height:3px;background:var(--ink);transform:rotate(45deg)}
.info .row .ico svg{width:7px;height:7px}
.info .row p{padding:1px 3px;font-weight:700}
.mix{display:grid;grid-template-columns:10px 1fr 22px 22px 38px 22px}
.mix > div{border-top:.6px solid var(--ink);border-right:.6px solid var(--ink);padding:1.5px 2px;font-weight:700;min-height:8px;display:flex;align-items:center;justify-content:center}
.mix > div:nth-child(6n){border-right:0}
.mix > div:nth-child(-n+6){border-top:0}
.mix .label{justify-content:flex-start}
.mix .dots{letter-spacing:.3px;font-size:4px}
.mix .ico i{width:3px;height:3px;background:var(--ink);transform:rotate(45deg)}
.back .maker{margin-top:8px;display:flex;align-items:center;justify-content:center;gap:3px}
.back .maker i{width:8px;height:8px;border-radius:50%;background:var(--blue)}
.back .maker span{font-family:"Archivo Black",sans-serif;font-size:5px;line-height:1.05}
.back .contact{margin-top:4px;text-align:center;font-size:3px;font-weight:700;line-height:1.35}
.back .weight{margin-top:5px}
</style>
</head>
<body>
<main class="dieline" aria-label="Larkfield Cement 42.25 bag dieline">

  <section class="panel flap flap--top">
    <span class="tag">EXPORT</span>
    <div class="grade"><b>42.25</b><span>CEMENT</span></div>
    <span class="tag">QUALITY</span>
  </section>

  <section class="panel side side--left">
    <div class="mark mark--top"><i></i><span>LARKFIELD</span></div>
    <div class="band"><span class="flip">CEMENT</span><span>CEMENT</span></div>
    <div class="mark mark--bottom"><i></i><span>LARKFIELD</span></div>
  </section>

  <section class="panel front">
    <svg viewBox="0 0 226 338" width="226" height="338" aria-hidden="true">
      <polygon points="22,0 204,0 190,26 36,26" fill="var(--yellow)"/>
      <polygon points="36,26 190,26 226,70 226,290 190,314 36,314 0,290 0,70" fill="var(--cream)"/>
      <polygon points="36,314 190,314 204,338 22,338" fill="var(--yellow)"/>
    </svg>
    <div class="content">
      <div class="emblem"></div>
      <div class="brand">LARKFIELD</div>
      <div class="product">
        <svg viewBox="0 0 156 40" width="156" height="40" aria-hidden="true"><polygon points="14,0 142,0 156,20 142,40 14,40 0,20" fill="var(--blue)"/></svg>
        <span>CEMENT</span>
      </div>
      <div class="origin"><span>EXPORT<br>QUALITY</span><span class="diamond"></span><span>PRODUCTS<br>MYANMAR</span></div>
      <div class="weight"><b>50</b><sup>KG</sup><span>NET WT.</span></div>
    </div>
    <div class="spec"><b>Portland Cement</b><span>EN 197-1 (2000) Strength Class 42.5</span></div>
  </section>

  <section class="panel side side--right">
    <div class="mark mark--top"><i></i><span>LARKFIELD</span></div>
    <div class="band"><span class="flip">CEMENT</span><span>CEMENT</span></div>
    <div class="mark mark--bottom"><i></i><span>LARKFIELD</span></div>
  </section>

  <section class="panel back">
    <div class="head">
      <i></i>
      <span class="brand-sm">LARKFIELD</span>
      <div class="grade-sm"><span>EXPORT</span><b>50.25</b><span>QUALITY</span></div>
      <span class="sub">CEMENT</span>
    </div>

    <div class="info">
      <h3>APPLICATIONS</h3>
      <div class="row"><div class="ico"><i></i></div><p>Suitable for general concrete products.</p></div>
    </div>

    <div class="info">
      <h3>MIXING INSTRUCTIONS</h3>
      <div class="mix">
        <div class="ico"><i></i></div><div class="label">Applications</div><div>Cement</div><div>Sand</div><div>Aggregate</div><div>Water</div>
        <div class="ico"><i></i></div><div class="label">Lean Concrete</div><div class="dots">●</div><div class="dots">●●●</div><div class="dots">●●●●●</div><div class="dots">●</div>
        <div class="ico"><i></i></div><div class="label">General Concrete</div><div class="dots">●</div><div class="dots">●●</div><div class="dots">●●●●</div><div>5 ct ●</div>
      </div>
    </div>

    <div class="info">
      <h3>RECOMMENDATIONS</h3>
      <div class="row"><div class="ico"><i></i></div><p>During 1-3 days of curing process,<br>concrete should be sprayed with water to avoid crack.</p></div>
      <div class="row"><div class="ico"><i></i></div><p>A bag of cement should be finished within 1 day. If not, seal the bag tightly.</p></div>
    </div>

    <div class="info">
      <h3>PRECAUTIONS</h3>
      <div class="row"><div class="ico"><svg viewBox="0 0 8 8" aria-hidden="true"><rect x="1.5" y="3" width="5" height="4" fill="none" stroke="var(--ink)" stroke-width=".8"/><path d="M4 3V1" stroke="var(--ink)" stroke-width=".8"/></svg></div><p>Lift with care.</p></div>
      <div class="row"><div class="ico"><svg viewBox="0 0 8 8" aria-hidden="true"><rect x="2" y="2" width="4" height="5" rx="1" fill="var(--ink)"/></svg></div><p>Wear gloves while mixing or handling dry cement.</p></div>
      <div class="row"><div class="ico"><svg viewBox="0 0 8 8" aria-hidden="true"><rect x="1.5" y="3" width="5" height="3" rx="1.2" fill="none" stroke="var(--ink)" stroke-width=".8"/></svg></div><p>Wear a mask while mixing dry cement.</p></div>
      <div class="row"><div class="ico"><svg viewBox="0 0 8 8" aria-hidden="true"><circle cx="4" cy="4" r="3" fill="none" stroke="var(--ink)" stroke-width=".8"/><path d="M2 6L6 2" stroke="var(--ink)" stroke-width=".8"/></svg></div><p>Keep cement away from child's reach.</p></div>
      <div class="row"><div class="ico"><svg viewBox="0 0 8 8" aria-hidden="true"><path d="M1 6H7M2 4H6" stroke="var(--ink)" stroke-width=".8"/></svg></div><p>Cement should be stored under shade and away from moisture with<br>pallets being raised above the ground.</p></div>
    </div>

    <div class="maker"><i></i><span>NORTHVALE<br>CEMENT CO., LTD.</span></div>
    <div class="contact">
      <p>No. 12, Harbor Road, Eastgate Township, Yangon, Myanmar</p>
      <p>T: +95 1 555 0142 · +95 1 555 0178 · E: info@northvalecement.com</p>
      <p>www.northvalecement.com</p>
    </div>
    <div class="weight"><b>50</b><sup>KG</sup><span>NET WT.</span></div>
  </section>

  <section class="panel flap flap--bottom">
    <span class="tag">EXPORT</span>
    <div class="grade"><b>42.25</b><span>CEMENT</span></div>
    <span class="tag">QUALITY</span>
  </section>

</main>
</body>
</html>
```